Print materials for 3-star hotel

We are changing up our print materials (notepads, letterheads, key card jackets, small flyer for the room rates) We are a 3 star business hotel in the Philippines and have mainly used grey tones and clean, simple lines. See attached photos for logo and hotel interior photos.

Target Market(s)

Business

Contact Information for Business Card

Corvina Terrace Hotel
Magistrate Lunod Avenue corner Pabilo St Cebu City 6000 Philippines
Tel: +63 32 481 7520
Mobile: +63 917 604 2893
www.corvinaterracehotel.example

Font styles to use
Serif
Sans Serif

Requirements
Must have
• Simple
• Readable font and font size
Nice to have
• Neutral colors, grey and taupes
Should not have
• No purples and bright blues

```html
<!DOCTYPE html>
<html lang="en">
<head>
<meta charset="utf-8">
<title>Corvina Terrace Hotel – Business Card</title>
<link rel="stylesheet" href="https://fonts.googleapis.com/css2?family=Cinzel:wght@400;500&family=Jost:wght@400&display=swap">
<style>
  :root {
    --backdrop: #ebe8e4;
    --card: #17191b;
    --gold: #b2a281;
    --gold-soft: #8f8268;
    --shadow: rgba(40, 32, 20, 0.22);
  }
  * { box-sizing: border-box; margin: 0; padding: 0; }
  html, body { width: 1200px; height: 997px; overflow: hidden; }
  body {
    background: var(--backdrop);
    position: relative;
    font-family: "Jost", "Futura", sans-serif;
    color: var(--gold);
  }
  .card {
    position: absolute;
    left: 250px;
    width: 700px;
    height: 400px;
    background: var(--card);
    box-shadow: 0 14px 30px var(--shadow);
  }
  .card--front { top: 70px; }
  .card--back { top: 527px; }

  /* front */
  .front-mark {
    position: absolute;
    inset: 0;
    display: flex;
    align-items: center;
    justify-content: center;
    gap: 16px;
  }
  .front-mark__square {
    width: 22px; height: 22px;
    background: var(--gold);
  }
  .front-mark__name {
    font-family: "Cinzel", "Trajan Pro", serif;
    font-weight: 400;
    font-size: 34px;
    letter-spacing: 6px;
    color: var(--gold);
  }

  /* back */
  .holder {
    position: absolute;
    left: 48px; top: 58px;
    font-family: "Cinzel", "Trajan Pro", serif;
    color: var(--gold);
  }
  .holder__name { font-size: 26px; letter-spacing: 2px; line-height: 1; }
  .holder__title { font-size: 15px; letter-spacing: 2px; margin-top: 6px; }

  .brand {
    position: absolute;
    right: 48px; top: 56px;
    text-align: right;
    font-family: "Cinzel", "Trajan Pro", serif;
    color: var(--gold-soft);
  }
  .brand__name { font-size: 20px; letter-spacing: 5px; line-height: 1.1; }
  .brand__sub { font-size: 13px; letter-spacing: 7px; margin-top: 6px; }
  .brand__square {
    display: inline-block; width: 30px; height: 30px;
    background: var(--gold-soft); margin-bottom: 10px;
  }
  .rule {
    position: absolute;
    height: 1px;
    background: var(--gold-soft);
  }
  .rule--brand { right: 48px; top: 160px; width: 290px; }
  .rule--base { left: 48px; right: 48px; top: 318px; }

  .contact {
    position: absolute;
    left: 48px; top: 168px;
    font-size: 15px;
    line-height: 21px;
    color: var(--gold);
  }
  .contact__address { margin-bottom: 8px; }
  .contact__list { list-style: none; }
  .contact__list li { display: flex; align-items: center; gap: 10px; }
  .contact__list svg { width: 13px; height: 13px; fill: var(--gold); flex: none; }

  .website {
    position: absolute;
    left: 48px; top: 330px;
    font-size: 15px;
    letter-spacing: 3px;
    color: var(--gold);
  }
</style>
</head>
<body>

<section class="card card--front" aria-label="Business card front">
  <div class="front-mark">
    <span class="front-mark__square"></span>
    <span class="front-mark__name">CORVINA TERRACE</span>
  </div>
</section>

<section class="card card--back" aria-label="Business card back">
  <div class="holder">
    <p class="holder__name">ELIAN NAVARRO</p>
    <p class="holder__title">PRESIDENT</p>
  </div>

  <div class="brand">
    <span class="brand__square"></span>
    <p class="brand__name">CORVINA TERRACE</p>
    <p class="brand__sub">HOTEL</p>
  </div>
  <div class="rule rule--brand"></div>

  <div class="contact">
    <p class="contact__address">27 Halden Crest Road<br>Cebu City 6000</p>
    <ul class="contact__list">
      <li>
        <svg viewBox="0 0 16 16"><path d="M3 1h3l1.5 4-2 1.3a9 9 0 0 0 4.2 4.2L11 8.5l4 1.5v3a2 2 0 0 1-2 2A12 12 0 0 1 1 3a2 2 0 0 1 2-2z"/></svg>
        +63 32 481 7520
      </li>
      <li>
        <svg viewBox="0 0 16 16"><path d="M4 0h8a1 1 0 0 1 1 1v14a1 1 0 0 1-1 1H4a1 1 0 0 1-1-1V1a1 1 0 0 1 1-1zm1 2v10h6V2zm3 11a1 1 0 1 0 0 2 1 1 0 0 0 0-2z"/></svg>
        +63 917 604 2893
      </li>
      <li>
        <svg viewBox="0 0 16 16"><path d="M4 1h8v4H4zM1 6h14v7h-3v2H4v-2H1zm4 5v3h6v-3z"/></svg>
        +63 32 481 7521
      </li>
      <li>
        <svg viewBox="0 0 16 16"><path d="M1 3h14v10H1zm1.5 1.2v.6L8 9l5.5-4.2v-.6z"/></svg>
        elian@corvinaterracehotel.example
      </li>
    </ul>
  </div>

  <div class="rule rule--base"></div>
  <p class="website">www.corvinaterracehotel.example</p>
</section>

</body>
</html>
```